Business Card Design

We are a manufacturing company that has been in business for over 30 years, established in 1981. We are looking to increase our business with defence force, government, and the major telecoms so the card needs to present the company as being cutting edge, secure, and professional.
Industry/Entity Type
Defence
Contact Information for Business Card
Name Gareth Olsund
Phone 02 9374 6815
Fax 02 9457 3162
mobile 0438260517
Email Gary@Korvex.com.au
Webiste www.korvex.com.au
ABN 58 006 391 842
address: 17 Belcor Street Tarrowdale NSW 2748
"Manufacturer of Antennas, GPS, Microwave, Cable Assemblies, RF, Military, & Telecommunications"
Look and feel

```html
<!DOCTYPE html>
<html lang="en">
<head>
<meta charset="utf-8">
<title>Korvex Business Card</title>
<link rel="stylesheet" href="https://fonts.googleapis.com/css2?family=Archivo:wght@700&family=Archivo+Narrow:wght@400;500&display=swap">
<style>
  :root {
    --navy: #1c2a5e;
    --rust: #c4432b;
    --paper: #ffffff;
    --backdrop: #e8e6e3;
    --ink-soft: #3a4470;
  }
  * { box-sizing: border-box; margin: 0; padding: 0; }
  html, body {
    width: 1200px; height: 1000px; overflow: hidden;
    background: var(--backdrop);
    font-family: "Archivo Narrow", "Arial Narrow", sans-serif;
  }
  .canvas {
    width: 1200px; height: 1000px;
    display: flex; flex-direction: column;
    align-items: center; justify-content: center; gap: 60px;
  }
  .card {
    position: relative;
    width: 640px; height: 366px;
    background: var(--paper);
    box-shadow: 0 6px 18px rgba(0,0,0,.12);
    overflow: hidden;
  }
  .brand {
    display: flex; align-items: center; gap: 10px;
    color: var(--rust);
    font-family: "Archivo Narrow", "Arial Narrow", sans-serif;
    font-weight: 500; letter-spacing: .22em; text-transform: uppercase;
  }
  .brand-square { background: var(--navy); flex: none; }

  /* Front */
  .card-front .brand { position: absolute; top: 28px; left: 30px; font-size: 16px; }
  .card-front .brand-square { width: 46px; height: 46px; }
  .abn {
    position: absolute; left: 30px; bottom: 26px;
    font-size: 11px; color: var(--ink-soft); letter-spacing: .03em;
  }
  .contact { position: absolute; left: 318px; top: 128px; width: 290px; }
  .contact-name {
    font-family: "Archivo", Arial, sans-serif; font-weight: 700;
    font-size: 22px; letter-spacing: .12em; text-transform: uppercase;
    color: var(--navy);
    padding-bottom: 4px; border-bottom: 2px solid var(--rust);
    margin-bottom: 12px;
  }
  .contact-list {
    display: grid; grid-template-columns: 74px 1fr;
    row-gap: 3px; font-size: 15px; color: var(--rust);
  }
  .contact-list dt { font-size: 13px; padding-top: 2px; }
  .contact-list .address-label { margin-top: 8px; }
  .contact-list .address { margin-top: 8px; line-height: 1.35; }

  /* Back */
  .tagline {
    position: absolute; top: 26px; right: 28px;
    text-align: right; color: var(--rust);
    font-size: 13px; letter-spacing: .06em; line-height: 1.3;
    text-transform: uppercase;
  }
  .card-back .brand {
    position: absolute; left: 50%; top: 50%;
    transform: translate(-50%, -50%);
    font-size: 30px; gap: 16px;
  }
  .card-back .brand-square { width: 84px; height: 84px; }
  .website {
    position: absolute; right: 40px; bottom: 40px;
    color: var(--rust); font-size: 14px; letter-spacing: .42em;
  }
</style>
</head>
<body>
<main class="canvas">
  <section class="card card-front" aria-label="Card front">
    <div class="brand"><span class="brand-square"></span>Korvex</div>
    <div class="contact">
      <h1 class="contact-name">Gareth Olsund</h1>
      <dl class="contact-list">
        <dt>Mobile:</dt><dd>04 3826 0517</dd>
        <dt>Phone:</dt><dd>02 9374 6815</dd>
        <dt>Fax:</dt><dd>02 9457 3162</dd>
        <dt>Email:</dt><dd>Gary@Korvex.com.au</dd>
        <dt class="address-label">Address:</dt>
        <dd class="address">17 Belcor Street<br>Tarrowdale<br>N.S.W. 2748</dd>
      </dl>
    </div>
    <p class="abn">abn 58 006 391 842</p>
  </section>

  <section class="card card-back" aria-label="Card back">
    <p class="tagline">Manufacturer of Antennas, GPS, Microwave,<br>Cable Assemblies, RF, Military, &amp; Telecommunications</p>
    <div class="brand"><span class="brand-square"></span>Korvex</div>
    <p class="website">www.korvex.com.au</p>
  </section>
</main>
</body>
</html>
```